Corporate marketing website with signup form

The function of the website is to promote our 2 product offerings. It will contain a main screen and several 5-7 sub-pages that will be available as 'scroll down' anchors and as front-page navigation links on the top of the page.

Navigation menu labels are: Products, Unique Model, Pricing, About, and Contact

Target Market(s)

Business to business marketers who are looking to source lead generation services

Industry/Entity Type

Marketing

Logo Text

VelQuora

Coding

Coded - Design and coding required

Number of Pages Required

5+ page

Requirements
Must have
• A sign-up form on main section of the front page. Fields are First Name, Last Name, Company, and Email (all text), and a pull-down with three options (only pick one): Track 1, Track 2, Custom Combination.
• Also incorporate the bottom half (ie crop the image) of the EPS file attached (the 'blue heads). Add this to the lower portion of the main screen and have the rest of the blue background become the background for the next anchored section of the navigation.
• You'll see the main section text in the mock-up I provided. The rest of the menu items/anchors can be lorem ipsum for now.
• Can this be coded in Wordpress? That would be my preference so I can edit it in the future.

```html
<!DOCTYPE html>
<html lang="en">
<head>
<meta charset="utf-8">
<title>VelQuora – Lead Generation Services</title>
<link rel="stylesheet" href="https://fonts.googleapis.com/css2?family=Bree+Serif&family=Francois+One&family=Lato:wght@400;700;900&display=swap">
<style>
:root{
  --blue:#1fa6de;
  --blue-dark:#1585bd;
  --ink:#222;
  --text:#555;
  --light:#f1f1f1;
  --navy:#1c2029;
  --navy-2:#262b35;
  --circle:rgba(18,22,30,.86);
  --orange:#f28c2a;
  --green:#58b031;
  --white:#fff;
  --grey-card:#e7e7e7;
}
*{box-sizing:border-box;margin:0;padding:0}
html,body{width:1200px;height:3199px;overflow:hidden}
body{position:relative;font-family:'Lato',sans-serif;color:var(--text);background:var(--white)}
.abs{position:absolute}
section,header,footer{position:absolute;left:0;width:1200px}

/* header */
.site-header{top:0;height:86px;background:var(--white);box-shadow:0 2px 6px rgba(0,0,0,.15);z-index:2}
.brand{left:141px;top:22px;display:flex;align-items:center;gap:10px}
.brand-dot{width:42px;height:42px;border-radius:50%;background:var(--blue)}
.brand-name{font-family:'Lato',sans-serif;font-weight:900;font-size:30px;color:#333;letter-spacing:.5px}
.main-nav{left:430px;top:33px;display:flex;gap:30px}
.main-nav a{font-size:14px;font-weight:700;color:#333;text-decoration:none;text-transform:uppercase;letter-spacing:.5px}
.main-nav a:first-child{color:var(--blue)}
.call{left:918px;top:22px;color:var(--blue)}
.call small{display:block;font-size:13px;font-weight:700;color:#666;margin-left:26px}
.call strong{display:flex;align-items:center;gap:6px;font-size:26px;font-weight:700}

/* hero */
.hero{top:86px;height:681px;overflow:hidden}
.hero-photo{position:absolute;inset:0;background:linear-gradient(180deg,#3b6a9a 0%,#6f9cc3 28%,#9bb3c2 50%,#8a8e86 72%,#6c6a62 100%)}
.hero h1{position:absolute;top:52px;width:100%;text-align:center;font-family:'Bree Serif',serif;font-weight:400;font-size:30px;color:var(--white)}
.hero h2{position:absolute;top:98px;width:100%;text-align:center;font-family:'Bree Serif',serif;font-weight:400;font-size:23px;color:var(--white)}
.track{position:absolute;top:199px;width:296px;height:296px;border-radius:50%;background:var(--circle);color:var(--white);text-align:center;padding:46px 46px 0;font-size:12px;line-height:16px}
.track h3{font-family:'Bree Serif',serif;font-weight:400;font-size:28px;line-height:32px;margin-bottom:8px}
.track p{margin-bottom:7px}
.track .hl{color:var(--blue)}
.track-1{left:125px}
.track-2{left:449px}
.track-2 h3{margin-top:22px}
.signup{position:absolute;left:808px;top:201px;width:288px;height:288px;border-radius:50%;background:var(--blue);border:5px solid rgba(255,255,255,.85);color:var(--white);text-align:center}
.signup h3{font-family:'Bree Serif',serif;font-weight:400;font-size:27px;margin-top:20px;line-height:28px}
.signup h4{font-weight:400;font-size:20px;line-height:22px}
.signup .row{display:flex;gap:6px;justify-content:center;margin-top:6px}
.field{height:26px;background:var(--white);color:#444;font-size:11px;text-align:left;padding:6px 8px;border-radius:2px}
.f-half{width:112px}
.f-full{width:230px}
.select{display:flex;justify-content:space-between}
.btn-submit{display:inline-block;margin-top:9px;width:110px;height:26px;border:1px solid var(--white);font-size:12px;font-weight:700;line-height:24px;letter-spacing:.5px}

/* section titles */
.sec-title{position:absolute;width:100%;text-align:center;font-family:'Francois One',sans-serif;font-weight:400;font-size:33px;color:var(--ink);letter-spacing:.5px}
.divider{position:absolute;left:530px;width:140px;height:14px}

/* products */
.products{top:767px;height:467px;background:var(--light)}
.product-img{position:absolute;top:132px;height:240px;border:2px solid var(--white);box-shadow:0 0 0 1px #ddd}
.pi-1{left:150px;width:433px;background:linear-gradient(135deg,#cfd6e0,#6b7c93 55%,#2c3646)}
.pi-2{left:633px;width:421px;background:linear-gradient(135deg,#3a3c3f,#9a9a98 50%,#dcdad6)}
.product-label{position:absolute;top:384px;font-weight:900;font-size:15px;color:var(--ink)}

/* models */
.models{top:1234px;height:490px;background:var(--white)}
.model{position:absolute;top:162px;width:223px}
.model-img{height:168px;border-radius:6px}
.m1{background:linear-gradient(135deg,#6f8aa3,#c3ccd4 60%,#3e4c5a)}
.m2{background:linear-gradient(135deg,#1f3b6e,#5d7fb0 50%,#c6d1df)}
.m3{background:linear-gradient(135deg,#1b3450,#3e6f93 50%,#0f1d2c)}
.m4{background:linear-gradient(135deg,#f1f1f1,#b9b9b9 60%,#6e6e6e)}
.model h4{font-weight:900;font-size:14px;color:var(--ink);margin-top:21px}
.model p{font-size:13px;line-height:19px;margin-top:4px}
.model a{display:block;font-size:12px;font-weight:700;color:var(--blue);margin-top:5px;text-decoration:none}

/* pricing */
.pricing{top:1724px;height:492px;background:linear-gradient(160deg,#27b0e6,#1a9fd8 60%,#1896cf)}
.pricing .sec-title{color:var(--white)}
.plan{position:absolute;top:150px;width:318px;height:262px;border-radius:6px;overflow:hidden;background:var(--grey-card);text-align:center;box-shadow:0 2px 5px rgba(0,0,0,.15)}
.plan-head{height:77px;background:var(--white);padding-top:14px;color:var(--ink);font-size:21px;line-height:24px}
.plan-head small{display:block;font-size:15px}
.price{margin-top:18px;font-weight:700;font-size:36px;color:var(--ink)}
.price span{font-size:13px;font-weight:400}
.plan p{font-size:13px;line-height:19px;margin:8px auto 0;width:230px}
.btn-plan{display:inline-block;margin-top:14px;width:118px;height:33px;line-height:33px;color:var(--white);font-size:13px;border-radius:2px}
.orange{background:var(--orange)}.blue{background:var(--blue)}.green{background:var(--green)}

/* about */
.about{top:2216px;height:325px;background:var(--white)}
.about-copy{position:absolute;left:150px;top:160px;width:900px;text-align:center;font-size:13px;line-height:22px}
.about-copy p{margin-bottom:10px}

/* contact */
.contact{top:2541px;height:658px;background:var(--navy)}
.contact .sec-title{color:var(--white)}
.input{position:absolute;border:1px solid #55606e;background:var(--navy-2);color:#aab;font-size:12px;font-style:italic;padding:10px 12px}
.btn-send{position:absolute;left:98px;top:383px;width:98px;height:36px;background:var(--blue);color:var(--white);font-size:12px;line-height:36px;text-align:center}
.map{position:absolute;left:644px;top:139px;width:460px;height:200px;background:linear-gradient(135deg,#e9e4d6,#d8dccb 50%,#c9d6e4)}
.info{position:absolute;left:648px;color:#ddd;font-size:12.5px;line-height:19px}
.info strong{color:var(--white)}
.info svg{position:absolute;left:0;top:2px}
.info div{margin-left:34px}
.heads{position:absolute;left:0;top:488px;width:1200px;height:125px;background:linear-gradient(180deg,var(--blue) 0%,var(--blue-dark) 100%)}
.copyright{position:absolute;left:0;top:613px;width:1200px;height:45px;line-height:45px;text-align:center;color:#ccc;font-size:12px;letter-spacing:.5px;background:var(--navy)}
</style>
</head>
<body>

<header class="site-header">
  <div class="brand abs"><span class="brand-dot"></span><span class="brand-name">VELQUORA</span></div>
  <nav class="main-nav abs">
    <a href="#products">Products</a>
    <a href="#unique-model">Unique Model</a>
    <a href="#pricing">Pricing</a>
    <a href="#about">About</a>
    <a href="#contact">Contact</a>
  </nav>
  <div class="call abs">
    <small>CALL US TODAY</small>
    <strong><svg width="18" height="18" viewBox="0 0 24 24"><path fill="#1fa6de" d="M6.6 10.8a15.1 15.1 0 0 0 6.6 6.6l2.2-2.2c.3-.3.7-.4 1-.2 1.1.4 2.3.6 3.6.6.6 0 1 .4 1 1V20c0 .6-.4 1-1 1A17 17 0 0 1 3 4c0-.6.4-1 1-1h3.5c.6 0 1 .4 1 1 0 1.3.2 2.5.6 3.6.1.3 0 .7-.2 1z"/></svg>123 555 0190</strong>
  </div>
</header>

<section class="hero" id="home">
  <div class="hero-photo" role="img" aria-label="Aerial photo of a coastal city skyline with high-rise towers and a beach"></div>
  <h1>List And Audience Building For Your Content Marketing Efforts</h1>
  <h2>We Offer 2 Tracks Form Which To Choose:</h2>

  <div class="track track-1">
    <h3>Track 1</h3>
    <p>Update, enhance or adppend your existing prospect database.</p>
    <p class="hl">Give us your ideal target title, company size and industry</p>
    <p>We provide contact lists derived from real-time data for your target including emails and phone numbers</p>
    <p>Coming soon: Discover what services &amp; technologies are being evaluated or used within your lists</p>
  </div>
  <div class="track track-2">
    <h3>Track 2</h3>
    <p>We use our data and email servers to send campaigns for you -</p>
    <p>You get access to all the campaign results back and only pay for actions: openers and clickers</p>
  </div>

  <form class="signup">
    <h3>Tell Us</h3>
    <h4>What You Want</h4>
    <div class="row"><div class="field f-half">First Name</div><div class="field f-half">Last Name</div></div>
    <div class="row"><div class="field f-full">Company</div></div>
    <div class="row"><div class="field f-full">Email</div></div>
    <div class="row"><div class="field f-full select"><span>Track</span><span>&#9662;</span></div></div>
    <div class="btn-submit">SUBMIT</div>
  </form>
</section>

<section class="products" id="products">
  <h2 class="sec-title" style="top:20px">PRODUCTS</h2>
  <svg class="divider" style="top:88px" viewBox="0 0 140 14"><line x1="0" y1="9" x2="58" y2="9" stroke="#bbb"/><line x1="82" y1="9" x2="140" y2="9" stroke="#bbb"/><rect x="63" y="3" width="14" height="9" fill="#999"/></svg>
  <div class="product-img pi-1" role="img" aria-label="Photo of two business people shaking hands"></div>
  <div class="product-img pi-2" role="img" aria-label="Photo of hands typing on a laptop keyboard"></div>
  <div class="product-label" style="left:150px">PRODUCTS 1</div>
  <div class="product-label" style="left:633px">PRODUCT 2</div>
</section>

<section class="models" id="unique-model">
  <h2 class="sec-title" style="top:54px">UNIQUE MODEL</h2>
  <svg class="divider" style="top:122px" viewBox="0 0 140 14"><line x1="0" y1="9" x2="58" y2="9" stroke="#bbb"/><line x1="82" y1="9" x2="140" y2="9" stroke="#bbb"/><rect x="63" y="3" width="14" height="9" fill="#999"/></svg>
  <article class="model" style="left:98px"><div class="model-img m1" role="img" aria-label="Photo of a laptop with digital interface graphics"></div><h4>MODEL 1</h4><p>Lorem Ipsum is simply dummy text of the printing and...</p><a href="#">More &rsaquo;</a></article>
  <article class="model" style="left:357px"><div class="model-img m2" role="img" aria-label="Illustration of interlocking strategy gears"></div><h4>MODEL 2</h4><p>Contrary to popular belief, Lorem Ipsum is not simply random text...</p><a href="#">More &rsaquo;</a></article>
  <article class="model" style="left:617px"><div class="model-img m3" role="img" aria-label="Photo of a person holding a tablet in a server room"></div><h4>MODEL 3</h4><p>Lorem Ipsum is simply dummy text of the printing ...</p><a href="#">More &rsaquo;</a></article>
  <article class="model" style="left:877px"><div class="model-img m4" role="img" aria-label="Sketch of business ideas drawn around a light bulb"></div><h4>MODEL 4</h4><p>There are many variations of passages of Lorem...</p><a href="#">More &rsaquo;</a></article>
</section>

<section class="pricing" id="pricing">
  <h2 class="sec-title" style="top:44px">PRICING</h2>
  <svg class="divider" style="top:112px" viewBox="0 0 140 14"><line x1="0" y1="9" x2="58" y2="9" stroke="#d6eefa"/><line x1="82" y1="9" x2="140" y2="9" stroke="#d6eefa"/><rect x="63" y="3" width="14" height="9" fill="#fff"/></svg>
  <div class="plan" style="left:98px"><div class="plan-head">Bronze<small>Package</small></div><div class="price">$ 199 <span>/ Month</span></div><p>Lorem Ipsum is simply dummy text of the printing and typesetting industry.</p><span class="btn-plan orange">Get it now</span></div>
  <div class="plan" style="left:440px"><div class="plan-head">Silver<small>Package</small></div><div class="price">$ 339 <span>/ Month</span></div><p>Lorem Ipsum is simply dummy text of the printing and typesetting industry.</p><span class="btn-plan blue">Get it now</span></div>
  <div class="plan" style="left:782px"><div class="plan-head">Gold<small>Package</small></div><div class="price">$ 689 <span>/ Month</span></div><p>Lorem Ipsum is simply dummy text of the printing and typesetting industry.</p><span class="btn-plan green">Get it now</span></div>
</section>

<section class="about" id="about">
  <h2 class="sec-title" style="top:43px">ABOUT VELQUORA</h2>
  <svg class="divider" style="top:111px" viewBox="0 0 140 14"><line x1="0" y1="9" x2="58" y2="9" stroke="#bbb"/><line x1="82" y1="9" x2="140" y2="9" stroke="#bbb"/><rect x="63" y="3" width="14" height="9" fill="#999"/></svg>
  <div class="about-copy">
    <p>Contrary to popular belief, Lorem Ipsum is not simply random text. It has roots in a piece of classical Latin literature from 45 BC, making it over 2000 years old. Edwin Harrow, a Latin professor at Larkfield College in Vermont, looked up one of the more obscure Latin words, consectetur, from a Lorem Ipsum passage, and going through the cites of the word in classical literature, discovered the undoubtable source.</p>
    <p>Lorem Ipsum is simply dummy text of the printing and typesetting industry. Lorem Ipsum has been the industry's standard dummy text ever since the 1500s, when an unknown printer took a galley of type and scrambled it to make a type specimen book.</p>
  </div>
</section>

<section class="contact" id="contact">
  <h2 class="sec-title" style="top:42px">CONTACT US</h2>
  <svg class="divider" style="top:110px" viewBox="0 0 140 14"><line x1="0" y1="9" x2="58" y2="9" stroke="#778"/><line x1="82" y1="9" x2="140" y2="9" stroke="#778"/><rect x="63" y="3" width="14" height="9" fill="#ccc"/></svg>
  <div class="input" style="left:98px;top:153px;width:241px;height:36px">Name</div>
  <div class="input" style="left:357px;top:153px;width:242px;height:36px">Phone No.</div>
  <div class="input" style="left:98px;top:212px;width:501px;height:36px">Email</div>
  <div class="input" style="left:98px;top:262px;width:501px;height:98px">Message</div>
  <div class="btn-send">SUBMIT</div>

  <div class="map" role="img" aria-label="Street map showing the office location"></div>
  <div class="info" style="top:361px">
    <svg width="16" height="20" viewBox="0 0 16 20"><path fill="#fff" d="M8 0a7 7 0 0 0-7 7c0 5 7 13 7 13s7-8 7-13a7 7 0 0 0-7-7zm0 10a3 3 0 1 1 0-6 3 3 0 0 1 0 6z"/></svg>
    <div><strong>VELQUORA</strong><br>123, Lorem Ipsum Dolor Sit Amet, Consectetur</div>
  </div>
  <div class="info" style="top:409px">
    <svg width="20" height="18" viewBox="0 0 24 24"><path fill="#fff" d="M6.6 10.8a15.1 15.1 0 0 0 6.6 6.6l2.2-2.2c.3-.3.7-.4 1-.2 1.1.4 2.3.6 3.6.6.6 0 1 .4 1 1V20c0 .6-.4 1-1 1A17 17 0 0 1 3 4c0-.6.4-1 1-1h3.5c.6 0 1 .4 1 1 0 1.3.2 2.5.6 3.6.1.3 0 .7-.2 1z"/></svg>
    <div>Call Us: 555-014-2288<br>Email Us: info@velquora.com</div>
  </div>

  <div class="heads" role="img" aria-label="Row of blue silhouettes of business people seen from behind"></div>
  <footer class="copyright">&copy; 2016 &nbsp;VELQUORA ALL RIGHTS RESERVED.</footer>
</section>

</body>
</html>
```